German tourism publishing house needs for international wellness hotel guide

We are planning as a print catalog. For this hotel directory we need a meaningful and appealing cover. The contents, a wide offer of wellness hotels should be recognizable at first sight. The title should make you want to go on a wellness holiday. The target group of the book are customers. We are looking forward to your next visit! The title "Wellness Hotels" should be larger on the cover written. The "Bravora logo" should be smaller on the cover. Please integrate the Internet address www.bravora-example.de small on the cover

Industry/Entity Type

Tourism

Font styles to use
Serif
Sans Serif

Colors
0355a3
ffffff
85acd3

Requirements
Must have
• We are looking forward to your next visit! The title "Wellness Hotels" should be larger on the cover written. The "Bravora logo" should be smaller on the cover.
Nice to have
• Please integrate the Internet address www.bravora-example.de small on the cover

```html
<!DOCTYPE html>
<html lang="en">
<head>
<meta charset="utf-8">
<title>Bravora – Wellness Hotels catalogue cover</title>
<link href="https://fonts.googleapis.com/css2?family=Dancing+Script:wght@700&family=Montserrat:wght@500&display=swap" rel="stylesheet">
<style>
  :root {
    --brand-blue: #0355a3;
    --light-blue: #85acd3;
    --white: #ffffff;
    --page-bg: #ffffff;
  }
  html, body {
    margin: 0;
    padding: 0;
    width: 1200px;
    height: 1200px;
    overflow: hidden;
    background: var(--page-bg);
  }
  .cover-spread {
    position: absolute;
    left: 30px;
    top: 231px;
    width: 1140px;
    height: 737px;
  }
  .cover-spread svg { display: block; width: 100%; height: 100%; }
  .brand-name {
    font-family: "Montserrat", sans-serif;
    font-weight: 500;
  }
  .web-address {
    font-family: "Montserrat", sans-serif;
    font-weight: 500;
  }
  .cover-title {
    font-family: "Dancing Script", cursive;
    font-weight: 700;
  }
</style>
</head>
<body>
<div class="cover-spread">
  <svg viewBox="0 0 1224 791" xmlns="http://www.w3.org/2000/svg">
    <defs>
      <linearGradient id="terraceTones" x1="0" y1="0" x2="0" y2="1">
        <stop offset="0" stop-color="#a9b9cc"/>
        <stop offset="0.22" stop-color="#6c6a45"/>
        <stop offset="0.45" stop-color="#9a4a3a"/>
        <stop offset="0.65" stop-color="#4a3a30"/>
        <stop offset="1" stop-color="#7d7570"/>
      </linearGradient>
      <linearGradient id="saunaTones" x1="0" y1="0" x2="1" y2="1">
        <stop offset="0" stop-color="#7a3d1c"/>
        <stop offset="1" stop-color="#c88a55"/>
      </linearGradient>
      <linearGradient id="restRoomTones" x1="0" y1="0" x2="0" y2="1">
        <stop offset="0" stop-color="#e3d6c8"/>
        <stop offset="1" stop-color="#a8734a"/>
      </linearGradient>
      <linearGradient id="readingTones" x1="0" y1="0" x2="1" y2="1">
        <stop offset="0" stop-color="#6e4f36"/>
        <stop offset="1" stop-color="#ece5dc"/>
      </linearGradient>
      <linearGradient id="poolTones" x1="0" y1="0" x2="0" y2="1">
        <stop offset="0" stop-color="#b9773a"/>
        <stop offset="0.6" stop-color="#f0c46a"/>
        <stop offset="1" stop-color="#4fb3c9"/>
      </linearGradient>
      <linearGradient id="frontTones" x1="0" y1="0" x2="0" y2="1">
        <stop offset="0" stop-color="#c3d1de"/>
        <stop offset="0.3" stop-color="#5f6f48"/>
        <stop offset="0.6" stop-color="#8b7a68"/>
        <stop offset="1" stop-color="#6e6864"/>
      </linearGradient>
      <clipPath id="collageClip">
        <path d="M0,440 C150,330 400,250 612,275 L612,300 C540,340 520,560 440,680 C380,760 250,768 0,760 Z"/>
      </clipPath>
    </defs>

    <!-- Back cover -->
    <g class="back-cover">
      <rect x="0" y="0" width="612" height="791" fill="var(--brand-blue)"/>
      <path class="photo-hotel-terrace" d="M0,0 H612 V300 L612,275 C400,250 150,330 0,440 Z" fill="url(#terraceTones)" role="img" aria-label="Hotel building with flower boxes and a wooden sun terrace with loungers"/>

      <g class="photo-collage" clip-path="url(#collageClip)">
        <rect x="0" y="260" width="265" height="250" fill="url(#saunaTones)" role="img" aria-label="Wooden sauna with candles"/>
        <rect x="265" y="260" width="347" height="250" fill="url(#restRoomTones)" role="img" aria-label="Relaxation room with wooden benches and panorama window"/>
        <rect x="0" y="510" width="190" height="260" fill="url(#readingTones)" role="img" aria-label="Guest in a bathrobe reading a magazine"/>
        <rect x="190" y="510" width="422" height="260" fill="url(#poolTones)" role="img" aria-label="Indoor pool under a timber ceiling"/>
        <line x1="265" y1="260" x2="265" y2="510" stroke="var(--white)" stroke-width="3"/>
        <line x1="0" y1="510" x2="612" y2="510" stroke="var(--white)" stroke-width="3"/>
        <line x1="190" y1="510" x2="190" y2="770" stroke="var(--white)" stroke-width="3"/>
      </g>
      <path class="collage-frame" d="M0,440 C150,330 400,250 612,275 M612,300 C540,340 520,560 440,680 C380,760 250,768 0,760" fill="none" stroke="var(--white)" stroke-width="8"/>
      <path class="inner-swoosh" d="M0,700 C20,600 70,500 150,440 C90,520 40,610 0,730 Z" fill="var(--brand-blue)" stroke="var(--white)" stroke-width="3"/>

      <text class="brand-name" x="494" y="724" text-anchor="middle" font-size="34" fill="var(--white)">Bravora</text>
      <text class="web-address" x="482" y="762" text-anchor="middle" font-size="14" letter-spacing="2" fill="var(--white)">www.bravora-example.de</text>
    </g>

    <!-- Front cover -->
    <g class="front-cover" transform="translate(612,0)">
      <rect class="photo-roof-terrace" x="0" y="0" width="612" height="733" fill="url(#frontTones)" role="img" aria-label="Roof terrace with wooden pergola, sun loungers and a daybed among trees"/>
      <text class="brand-name" x="530" y="88" text-anchor="middle" font-size="34" fill="var(--brand-blue)">Bravora</text>
      <g class="cover-title" fill="var(--brand-blue)" stroke="var(--white)" stroke-width="10" paint-order="stroke" stroke-linejoin="round" text-anchor="middle">
        <text x="310" y="225" font-size="118">Wellness</text>
        <text x="320" y="335" font-size="118">Hotels</text>
      </g>
      <rect x="0" y="733" width="612" height="58" fill="var(--brand-blue)"/>
      <text class="web-address" x="306" y="768" text-anchor="middle" font-size="17" letter-spacing="7" fill="var(--white)">www.bravora-example.de</text>
    </g>
  </svg>
</div>
</body>
</html>
```